Business Card Design, including supply of raw art files plus a vector diagram of the flenzo logo and

We need the business card design for a company that is launching a new exciting product. The brief requires the submission of the following once the final design is chosen:

- business card layout including raw files
- a composite vector image file of the flenzo logo and tag line
- a standalone vector image file of the flenzo logo

The product will be launched as a customer engagement app.

It has 4 core modules which enables a person to do multiple things - book tours and activities, order takeaways, search for local deals and offers. A universal currency is at the heart of this product. When you use the app, you earn cashback rewards when shopping or buying at any of the merchant partners across the modules as . These rewards can then be used as full or part payment when buying goods or services at these merchant partners.

The business card must help us build the brand, communicate the benefit of the brand's key focus - the ability to earn and burn this universal cashback ccurrency - across the 4 modules - booking of tours and activities, ordering, searching for local deals and payment.

We would like the design to use the brand's blue colour the hex colour is: 00
Dark grey : 646464
Darker blue shadow: 058bdd
Main Blue: 0084ff

We need to translate this into a CMYK print or spot colour print.

Both print options to be supplied as separate files.

An example of the base concept we have in mind is attached for your reference.

The font used by the brand is Proxima Nova.

Industry/Entity Type

Business

Contact Information for Business Card

Carla Whitfield
Marketing
W: www.flenzo.co
M: + 61 407318265
T: +61 2 9375 4120
A: Suite 7, Level 2, 14-18 Harrow Lane, Sydney, NSW, 2000, Australia

Font styles to use
Sans Serif

Requirements
Must have
• flEnzo logo and tagline
• address details
• flEnzo icons as supplied
Nice to have
• would like to have the option of a spot varnish layer over the logo and icons at the back of the card

```html
<!DOCTYPE html>
<html lang="en">
<head>
<meta charset="utf-8">
<title>flEnzo Business Card</title>
<link href="https://fonts.googleapis.com/css2?family=Montserrat:wght@200;400;600;700&display=swap" rel="stylesheet">
<style>
  :root {
    --bg: #e6e7e9;
    --card-grey: #4a4a4c;
    --brand-blue: #3a98d8;
    --line-blue: #2f8fd6;
    --white: #ffffff;
    --ink: #4c4c4e;
    --muted: #8a8a8c;
  }
  * { margin: 0; padding: 0; box-sizing: border-box; }
  html, body { width: 1200px; height: 900px; overflow: hidden; }
  body {
    background: var(--bg);
    font-family: "Montserrat", sans-serif;
    position: relative;
  }
  .card {
    position: absolute;
    left: 250px;
    width: 700px;
    height: 400px;
    border-radius: 26px;
    overflow: hidden;
  }
  /* Back */
  .card-back { top: 35px; background: var(--card-grey); }
  .back-mark {
    position: absolute; left: 260px; top: 90px;
    width: 180px; height: 180px; border-radius: 50%;
    background: var(--brand-blue);
    display: flex; align-items: center; justify-content: center;
  }
  .back-mark .brand-name {
    color: var(--white); font-weight: 400; font-size: 38px; letter-spacing: 1px;
  }
  .modules {
    position: absolute; right: 32px; bottom: 40px;
    display: flex; gap: 14px; align-items: flex-end;
  }
  .module { display: flex; flex-direction: column; align-items: center; gap: 5px; }
  .module svg { width: 30px; height: 30px; }
  .module-label {
    color: var(--white); font-size: 5.5px; font-weight: 600; letter-spacing: .3px; white-space: nowrap;
  }
  /* Front */
  .card-front { top: 465px; background: var(--card-grey); }
  .front-top {
    position: absolute; left: 0; top: 0; width: 100%; height: 200px;
    background: var(--white);
    border-bottom: 5px solid var(--line-blue);
  }
  .logo-lockup {
    position: absolute; left: 150px; top: 52px;
    display: flex; align-items: center; gap: 20px;
  }
  .logo-dot { width: 96px; height: 96px; border-radius: 50%; background: var(--brand-blue); }
  .wordmark .brand-name {
    display: block; font-weight: 200; font-size: 72px; color: var(--ink); line-height: 1; letter-spacing: 1px;
  }
  .tagline {
    display: block; font-weight: 200; font-size: 22px; color: var(--muted); letter-spacing: 1px; margin-top: 2px;
  }
  .person {
    position: absolute; right: 370px; top: 228px; text-align: right; color: var(--white);
  }
  .person-name { font-weight: 700; font-size: 24px; }
  .person-role { font-weight: 400; font-size: 15px; margin-top: 2px; }
  .address { font-weight: 400; font-size: 15px; line-height: 1.45; margin-top: 16px; }
  .divider {
    position: absolute; left: 350px; top: 228px; width: 1px; height: 120px; background: #9a9a9c;
  }
  .contacts {
    position: absolute; left: 372px; top: 224px; list-style: none; color: var(--white);
    font-size: 14.5px; line-height: 25px;
  }
  .contacts li { display: flex; align-items: center; gap: 12px; }
  .contacts svg { width: 12px; height: 12px; flex: none; }
  .contacts b { font-weight: 700; }
</style>
</head>
<body>

<section class="card card-back" aria-label="Card back">
  <div class="back-mark"><span class="brand-name">flEnzo</span></div>
  <div class="modules">
    <div class="module">
      <svg viewBox="0 0 30 30"><circle cx="15" cy="15" r="11" fill="var(--brand-blue)"/><path d="M10 15l4 4 7-8" stroke="#fff" stroke-width="2.5" fill="none"/></svg>
      <span class="module-label">CASHBACK REWARDS</span>
    </div>
    <div class="module">
      <svg viewBox="0 0 30 30"><rect x="3" y="3" width="24" height="24" fill="var(--brand-blue)"/></svg>
      <span class="module-label">TOURS ACTIVITIES</span>
    </div>
    <div class="module">
      <svg viewBox="0 0 30 30"><rect x="3" y="9" width="24" height="16" rx="3" fill="var(--brand-blue)"/><rect x="10" y="5" width="10" height="6" rx="1" fill="var(--brand-blue)"/><circle cx="15" cy="17" r="5" fill="var(--card-grey)"/><circle cx="15" cy="17" r="3" fill="var(--brand-blue)"/></svg>
      <span class="module-label">MOBILE ORDERING</span>
    </div>
    <div class="module">
      <svg viewBox="0 0 30 30"><path d="M6 4l18 22M24 4L6 26" stroke="var(--brand-blue)" stroke-width="3"/></svg>
      <span class="module-label">LOCAL OFFERS</span>
    </div>
    <div class="module">
      <svg viewBox="0 0 30 30"><rect x="3" y="3" width="24" height="24" fill="var(--brand-blue)"/></svg>
      <span class="module-label">&nbsp;</span>
    </div>
  </div>
</section>

<section class="card card-front" aria-label="Card front">
  <div class="front-top">
    <div class="logo-lockup">
      <div class="logo-dot"></div>
      <div class="wordmark">
        <span class="brand-name">flEnzo</span>
        <span class="tagline">the cloud currency</span>
      </div>
    </div>
  </div>

  <div class="person">
    <div class="person-name">Carla Whitfield</div>
    <div class="person-role">Marketing</div>
    <div class="address">Suite 7, Level 2, 14-18 Harrow Lane<br>Sydney, NSW, 2000, Australia</div>
  </div>

  <div class="divider"></div>

  <ul class="contacts">
    <li><svg viewBox="0 0 12 12"><rect x="3" y="1" width="6" height="10" rx="1" fill="none" stroke="#fff"/></svg>+ 61 407318265</li>
    <li><svg viewBox="0 0 12 12"><path d="M2 1l3 0 1 3-1.5 1a6 6 0 0 0 3 3L9 6.5l3 1V11C6 11 1 6 1 1z" fill="#fff"/></svg>+61 2 9375 4120</li>
    <li><svg viewBox="0 0 12 12"><rect x="1" y="5" width="10" height="5" fill="#fff"/><rect x="3" y="2" width="6" height="3" fill="#fff"/></svg>+61 2 9375 4133</li>
    <li><svg viewBox="0 0 12 12"><circle cx="6" cy="6" r="5" fill="#fff"/></svg>www.<b>flenzo</b>.co</li>
    <li><svg viewBox="0 0 12 12"><rect x="1" y="2.5" width="10" height="7" fill="none" stroke="#fff"/><path d="M1 2.5l5 4 5-4" fill="none" stroke="#fff"/></svg>carla.whitfield@mailnorth.com</li>
  </ul>
</section>

</body>
</html>
```